Mosquito Repellent Wet Wipes pacakage design

We are a mosquito repellent manufacturer under the brand name "Zest Guard". We have a product currently and are looking to make it more attractive.

Our product is a mosquito repellent wipe that can be applied on skin and clothing for protection against mosquitoes. It is going to be available in sachets. Customer age groups include ages 10-30 as well as Moms who are key decision makers.

We are looking for a friendly package in terms of color and appeal and a redesign of Zest Guard logo. I am attaching our current product pictures and brochure. Hope this gets you started. We are attaching information on the spray bottle.

Visit www.tolvanhealthworks.com for more details.

Package Dimension Folded : 80x60 mm
Package Dimension unfolded: 80 x 120 mm

Thank you
Varun
Updates

Project Deadline Extended Reason: Still not happy with the designs that are submitted. Like to see more designs. Added Thursday, February 18, 2016

Target Market(s)

General population with more focus on age groups 10-30 as well as Moms

Industry/Entity Type

Cosmetics

Requirements
Must have
• Statutory information should be provided on the product including Manufacturing address, ingredient name & bar code. I guess we can do this once the package is finalized

```html
<!DOCTYPE html>
<html lang="en">
<head>
<meta charset="UTF-8">
<title>Zest Guard Insect Repellent Wipes – Sachet</title>
<link rel="stylesheet" href="https://fonts.googleapis.com/css2?family=Fredoka:wght@700&family=Roboto+Condensed:wght@400&family=Nunito:wght@400;800&display=swap">
<style>
  :root {
    --canvas-bg: #ffffff;
    --sachet-yellow: #f7d600;
    --sachet-white: #f6f6f6;
    --ink: #1c1c1c;
    --tagline-grey: #8a8a8a;
    --crimp: rgba(0, 0, 0, 0.08);
  }
  * { box-sizing: border-box; margin: 0; padding: 0; }
  html, body {
    width: 1200px;
    height: 1200px;
    overflow: hidden;
    background: var(--canvas-bg);
  }
  .canvas {
    position: relative;
    width: 1200px;
    height: 1200px;
  }
  .sachet {
    position: absolute;
    left: 150px;
    top: 50px;
    width: 900px;
    height: 1080px;
    background: var(--sachet-white);
    overflow: hidden;
  }
  .sachet__serration {
    position: absolute;
    left: 0;
    width: 100%;
    height: 14px;
    display: block;
  }
  .sachet__serration--top { top: 0; }
  .sachet__serration--bottom { bottom: 0; }
  .sachet__front {
    position: absolute;
    left: 0;
    top: 0;
    width: 100%;
    height: 820px;
    background: var(--sachet-yellow);
  }
  .sachet__crimp {
    position: absolute;
    left: 0;
    width: 100%;
    height: 50px;
    background: repeating-linear-gradient(
      to bottom,
      var(--crimp) 0 2px,
      transparent 2px 7px
    );
  }
  .sachet__crimp--top { top: 14px; }
  .sachet__crimp--bottom { bottom: 14px; }
  .product-name {
    position: absolute;
    left: 0;
    top: 130px;
    width: 100%;
    text-align: center;
    font-family: "Fredoka", sans-serif;
    font-weight: 700;
    font-size: 128px;
    line-height: 1;
    letter-spacing: -1px;
    color: var(--ink);
  }
  .product-type {
    position: absolute;
    left: 0;
    top: 300px;
    width: 100%;
    text-align: center;
    font-family: "Roboto Condensed", sans-serif;
    font-weight: 400;
    font-size: 44px;
    color: var(--ink);
  }
  .no-mosquito-art {
    position: absolute;
    left: 335px;
    top: 395px;
    width: 230px;
    height: 230px;
    border-radius: 50%;
    background: radial-gradient(circle, #fbe14a 0%, #fbe14a 52%, #ffffff 53%, #ffffff 62%, var(--sachet-yellow) 63%);
  }
  .protection-claim {
    position: absolute;
    left: 0;
    top: 710px;
    width: 100%;
    text-align: center;
    font-family: "Nunito", sans-serif;
    font-weight: 800;
    font-size: 34px;
    line-height: 1.25;
    letter-spacing: -0.5px;
    color: var(--ink);
  }
  .maker {
    position: absolute;
    left: 0;
    top: 880px;
    width: 100%;
    display: flex;
    flex-direction: column;
    align-items: center;
  }
  .maker__name {
    font-family: "Nunito", sans-serif;
    font-weight: 800;
    font-size: 50px;
    line-height: 1;
    color: var(--ink);
  }
  .maker__tagline {
    margin-top: 8px;
    font-family: "Nunito", sans-serif;
    font-weight: 400;
    font-size: 17px;
    color: var(--tagline-grey);
  }
  .pack-count,
  .pack-benefit {
    position: absolute;
    top: 968px;
    font-family: "Nunito", sans-serif;
    font-weight: 400;
    font-size: 28px;
    line-height: 1;
    color: var(--ink);
  }
  .pack-count { left: 68px; }
  .pack-benefit { right: 68px; }
</style>
</head>
<body>
<div class="canvas">
  <div class="sachet">
    <div class="sachet__front"></div>
    <div class="sachet__crimp sachet__crimp--top"></div>
    <div class="sachet__crimp sachet__crimp--bottom"></div>

    <svg class="sachet__serration sachet__serration--top" viewBox="0 0 900 14" preserveAspectRatio="none" aria-hidden="true">
      <pattern id="teeth-top" width="12" height="14" patternUnits="userSpaceOnUse">
        <polygon points="0,0 6,14 12,0" fill="#ffffff"/>
      </pattern>
      <rect width="900" height="14" fill="#f7d600"/>
      <rect width="900" height="14" fill="url(#teeth-top)"/>
    </svg>
    <svg class="sachet__serration sachet__serration--bottom" viewBox="0 0 900 14" preserveAspectRatio="none" aria-hidden="true">
      <pattern id="teeth-bottom" width="12" height="14" patternUnits="userSpaceOnUse">
        <polygon points="0,14 6,0 12,14" fill="#ffffff"/>
      </pattern>
      <rect width="900" height="14" fill="#f6f6f6"/>
      <rect width="900" height="14" fill="url(#teeth-bottom)"/>
    </svg>

    <h1 class="product-name">ZEST GUARD</h1>
    <p class="product-type">Inspect Repellent Wipes</p>

    <div class="no-mosquito-art" role="img" aria-label="Mosquito silhouette inside a prohibition sign"></div>

    <p class="protection-claim">Repels Mosquitoes that may carry<br>Malaria, Chikungunya, Dengue</p>

    <div class="maker">
      <div class="maker__name">Tolvan Care</div>
      <div class="maker__tagline">Everyday Care for Every Family</div>
    </div>

    <p class="pack-count">1 wipe</p>
    <p class="pack-benefit">long lasting</p>
  </div>
</div>
</body>
</html>
```